BrovaLT BIZ Card, email signature & Stationary

Professional business cards, email signatures and ms word letterhead

Target Market(s)

business owners

Industry/Entity Type

cloud hosting

Contact Information for Business Card

name title office phone number , direct line, fax email address web site

Font styles to use
Other font styles liked:
• something that compliments font in logo

```html
<!DOCTYPE html>
<html lang="en">
<head>
<meta charset="utf-8">
<title>BrovaLT HTML Email Signature</title>
<link href="https://fonts.googleapis.com/css2?family=Montserrat:wght@300;400;500;700;800&family=Open+Sans:wght@400&display=swap" rel="stylesheet">
<style>
  :root {
    --brand-red: #e31e24;
    --ink: #111111;
    --text-grey: #3a3a3a;
    --ui-grey: #4a4a4a;
    --ui-muted: #6b6b6b;
    --ribbon-bg: #f3f4f6;
    --ui-border: #d4d4d4;
    --page: #ffffff;
  }
  * { margin: 0; padding: 0; box-sizing: border-box; }
  html, body { width: 1200px; height: 1200px; overflow: hidden; background: var(--page); }
  .canvas { position: relative; width: 1200px; height: 1200px; font-family: "Montserrat", sans-serif; }

  .headline {
    position: absolute; top: 62px; left: 0; width: 100%;
    text-align: center; font-size: 46px; letter-spacing: 0.5px; line-height: 1;
  }
  .headline .strong { font-weight: 800; color: var(--ink); }
  .headline .light { font-weight: 300; color: var(--brand-red); }

  .ribbon {
    position: absolute; top: 182px; left: 0; width: 1200px; height: 33px;
    background: var(--ribbon-bg); border-bottom: 1px solid #e2e2e2;
    font-family: "Open Sans", sans-serif; font-size: 16px; color: var(--ui-grey);
  }
  .ribbon-group { position: absolute; top: 0; height: 33px; line-height: 38px; text-align: center; border-right: 1px solid #dcdcdc; }
  .ribbon-group.clipboard { left: 0; width: 258px; }
  .ribbon-group.basic-text { left: 258px; width: 496px; }
  .ribbon-group.names { left: 754px; width: 153px; }
  .ribbon-group.include { left: 907px; width: 237px; }
  .launcher { position: absolute; top: 15px; width: 8px; height: 8px; border: 1px solid #9a9a9a; border-width: 1px 0 0 1px; }
  .clipboard .launcher { right: 12px; }
  .basic-text .launcher { right: 12px; }

  .compose { font-family: "Open Sans", sans-serif; color: var(--ui-grey); }
  .send-button {
    position: absolute; left: 8px; top: 237px; width: 63px; height: 100px;
    border: 1px solid var(--ui-border); background: #fafafa; text-align: center; font-size: 16px;
  }
  .send-button svg { display: block; margin: 24px auto 14px; }
  .field-button {
    position: absolute; left: 86px; width: 82px; height: 29px;
    border: 1px solid var(--ui-border); background: #fafafa;
    font-size: 16px; line-height: 27px; text-align: center;
  }
  .field-button.from { top: 237px; }
  .field-button.to { top: 273px; }
  .field-button.cc { top: 308px; }
  .caret { display: inline-block; width: 0; height: 0; border-left: 6px solid transparent; border-right: 6px solid transparent; border-top: 6px solid var(--ui-grey); vertical-align: middle; margin-left: 4px; }
  .sender-address { position: absolute; left: 190px; top: 241px; font-size: 16px; color: var(--ui-muted); }
  .subject-label { position: absolute; left: 86px; top: 347px; font-size: 16px; color: var(--ui-muted); }
  .input-field { position: absolute; left: 182px; width: 1018px; height: 29px; border: 1px solid var(--ui-border); border-right: none; background: var(--page); }
  .input-field.to { top: 274px; }
  .input-field.cc { top: 309px; }
  .input-field.subject { top: 344px; }
  .body-rule { position: absolute; left: 8px; top: 383px; width: 1192px; height: 1px; background: var(--ui-border); }
  .body-edge { position: absolute; left: 8px; width: 1px; background: var(--ui-border); }
  .body-edge.upper { top: 383px; height: 50px; }
  .body-edge.lower { top: 690px; height: 167px; }

  .signature { position: absolute; left: 68px; top: 440px; }
  .sig-name { font-size: 25px; font-weight: 700; color: var(--ink); line-height: 1.05; }
  .sig-title { font-size: 20px; font-weight: 500; color: var(--brand-red); line-height: 1.1; }
  .sig-address { margin-top: 24px; font-size: 20.5px; color: var(--text-grey); line-height: 25px; }
  .sig-contacts { margin-top: 8px; font-size: 20.5px; color: var(--text-grey); line-height: 25.5px; display: grid; grid-template-columns: 168px auto; }
  .label { color: var(--brand-red); }
  .social-row { display: flex; gap: 7px; margin-top: 20px; }
  .social-square { width: 30px; height: 30px; background: var(--brand-red); border-radius: 3px; }
  .wordmark { margin-top: 24px; font-size: 60px; font-weight: 400; color: var(--brand-red); line-height: 1; letter-spacing: -1px; }
</style>
</head>
<body>
<div class="canvas">
  <h1 class="headline"><span class="strong">HTML EMAIL</span> <span class="light">SIGNATURE</span></h1>

  <div class="ribbon">
    <div class="ribbon-group clipboard">Clipboard<span class="launcher"></span></div>
    <div class="ribbon-group basic-text">Basic Text<span class="launcher"></span></div>
    <div class="ribbon-group names">Names</div>
    <div class="ribbon-group include">Include</div>
  </div>

  <div class="compose">
    <div class="send-button">
      <svg width="42" height="24" viewBox="0 0 42 24" aria-hidden="true">
        <rect x="6" y="2" width="34" height="20" fill="#fff" stroke="#9a9a9a"/>
        <line x1="14" y1="13" x2="28" y2="13" stroke="#b5b5b5"/>
        <line x1="1" y1="5" x2="5" y2="5" stroke="#9a9a9a"/>
        <line x1="2" y1="9" x2="5" y2="9" stroke="#9a9a9a"/>
        <rect x="34" y="4" width="4" height="5" fill="#2d6fb5"/>
      </svg>
      Send
    </div>
    <div class="field-button from">From<span class="caret"></span></div>
    <div class="field-button to">To...</div>
    <div class="field-button cc">Cc...</div>
    <div class="sender-address">PaulR@Norwick.com</div>
    <div class="subject-label">Subject</div>
    <div class="input-field to"></div>
    <div class="input-field cc"></div>
    <div class="input-field subject"></div>
    <div class="body-rule"></div>
    <div class="body-edge upper"></div>
    <div class="body-edge lower"></div>
  </div>

  <div class="signature">
    <div class="sig-name">DORIAN VELASKO</div>
    <div class="sig-title">Founder &amp; CEO</div>
    <div class="sig-address">Corvel Ave Suite<br>B4 Marlow, OR 97301</div>
    <div class="sig-contacts">
      <span><span class="label">P :</span> 555.310.4820</span><span><span class="label">E :</span> dorian@brovalt.com</span>
      <span><span class="label">F :</span> 555.310.4821</span><span><span class="label">W :</span> www.brovaltweb.com</span>
    </div>
    <div class="social-row">
      <div class="social-square" role="img" aria-label="Social profile link"></div>
      <div class="social-square" role="img" aria-label="Social profile link"></div>
      <div class="social-square" role="img" aria-label="Social profile link"></div>
    </div>
    <div class="wordmark">BrovaLT</div>
  </div>
</div>
</body>
</html>
```